Criminal Defense Lawyer Business Card

I am starting a new criminal defense law office in New Jersey and I need a business card for potential clients. I plan to use technology to increase the client's connection with their criminal defense. I wish to use the motto: "Stand Firm With Your Counsel."
I have a QR code that I would ask you to consider including in the design.
Attached are samples from the current draft card.

The people looking at this card are frightened and seeking someone who can help them with their unexpected arrest.
The final design should communicate sophistication, technological skill, and aggressive representation.
Updates

Reason: Final review of designs. Thank you for the designs.

Target Market(s)

Industry/Entity Type

Defense

Contact Information for Business Card

Everett Lansford
(844) TX Shielded – toll free
(844) 917-4403
(609) 481-7725
(732) 604-1159
(908) 273-6641

Rett@TX Shielded.com
www.TX Shielded.com

“Stand Firm With Your Counsel”

Law Office of Everett Lansford, L.L.C.

Former State & Federal Prosecutor – 15 Years Experience
Contact Now for a Free Initial Consultation

Requirements
Must have
• “Stand Firm With Your Counsel”
TXShielded.com
Nice to have
• Aggressive Criminal Defense & DUI Defense

QR code is the logo. (Ignore if you feel design is better without the QR code)
Should not have
• May not say "specialist" or "specialize" or claim to be the best. (New Jersey lawyer rules.)
Address is intentionally left off.

```html
<!DOCTYPE html>
<html lang="en">
<head>
<meta charset="utf-8">
<title>Everett Lansford – Business Card</title>
<link href="https://fonts.googleapis.com/css2?family=Marcellus+SC&family=Yanone+Kaffeesatz:wght@400;500&display=swap" rel="stylesheet">
<style>
  :root {
    --stage: #e9e6e1;
    --card: #0b2530;
    --band: #0f3a48;
    --band-soft: #12404e;
    --ring: #1d7f91;
    --tagline: #2a6474;
    --ink: #f4f7f8;
    --ink-dark: #07171d;
    --glow-center: #c8d3d8;
    --glow-edge: #163a47;
  }
  * { box-sizing: border-box; margin: 0; padding: 0; }
  html, body { width: 1200px; height: 900px; overflow: hidden; }
  body { background: var(--stage); position: relative; font-family: "Yanone Kaffeesatz", "Arial Narrow", sans-serif; color: var(--ink); }

  .card {
    position: absolute; top: 100px; width: 400px; height: 700px;
    background: var(--card); overflow: hidden;
    box-shadow: 0 10px 28px rgba(0,0,0,.25);
  }
  .card--back { left: 160px; }
  .card--front { left: 640px; }

  .crest-band {
    position: absolute; left: 100px; top: 0; width: 200px; height: 255px;
    background: var(--band); border-radius: 0 0 100px 100px;
  }
  .emblem {
    position: absolute; left: 112px; width: 176px; height: 176px; border-radius: 50%;
    border: 3px solid var(--ring);
    background: radial-gradient(circle at 50% 40%, var(--glow-center) 0%, #6d8791 28%, var(--glow-edge) 70%);
  }
  .card--back .emblem { top: 62px; }
  .card--front .emblem { top: 78px; }

  .tagline {
    position: absolute; left: 0; width: 100%; text-align: center;
    color: var(--tagline); font-size: 23px; letter-spacing: .3px;
  }
  .card--back .tagline { top: 266px; }
  .card--front .tagline { top: 282px; }

  .firm {
    position: absolute; top: 304px; width: 100%; text-align: center;
    font-size: 25px; line-height: 30px; font-weight: 500;
  }
  .consult {
    position: absolute; top: 430px; width: 100%; text-align: center;
    font-family: "Marcellus SC", Georgia, serif; font-size: 25px; line-height: 28px; letter-spacing: .5px;
  }
  .links { position: absolute; top: 530px; left: 0; width: 100%; }
  .link {
    display: flex; align-items: center; justify-content: center; gap: 12px;
    font-size: 32px; font-weight: 500; height: 46px;
  }
  .link svg { width: 26px; height: 26px; flex: none; }

  .site-top {
    position: absolute; top: 24px; width: 100%; text-align: center;
    font-size: 22px; font-weight: 500;
  }
  .name {
    position: absolute; top: 330px; width: 100%; text-align: center;
    font-family: "Marcellus SC", Georgia, serif; font-size: 38px; font-weight: 400; letter-spacing: 1px;
  }
  .title-strip {
    position: absolute; top: 382px; left: 0; width: 100%; height: 44px;
    background: var(--band-soft);
    font-family: "Marcellus SC", Georgia, serif; font-size: 27px; letter-spacing: 1.5px;
    color: var(--ink-dark); text-align: center; line-height: 44px;
  }
  .phones {
    position: absolute; top: 446px; left: 0; width: 100%;
    display: grid; grid-template-columns: 1fr 1fr; row-gap: 4px; column-gap: 14px;
    padding: 0 40px; font-size: 26px; font-weight: 500;
  }
  .phones .toll { grid-column: 1 / 3; text-align: center; }
  .phones span:nth-child(even) { text-align: right; }
  .phones span:nth-child(odd):not(.toll) { text-align: left; }

  .specialty-band {
    position: absolute; left: 0; bottom: 0; width: 100%; height: 112px;
    background: var(--band); border-top: 4px solid var(--band-soft);
  }
  .specialty-band p {
    position: absolute; top: 50px; width: 100%; text-align: center;
    font-size: 29px; font-weight: 500;
  }
</style>
</head>
<body>

  <section class="card card--back">
    <div class="crest-band"></div>
    <div class="emblem" role="img" aria-label="Scales of justice emblem in a glowing circle"></div>
    <p class="tagline">“Stand Firm With Your Counsel”</p>
    <p class="firm">Law Office of Everett Lansford, L.L.C.<br>Former State &amp; Federal Prosecutor<br>15 Years Experience</p>
    <p class="consult">Contact Now for a Free<br>Initial Consultation</p>
    <div class="links">
      <p class="link">
        <svg viewBox="0 0 26 26" aria-hidden="true"><rect x="2" y="6" width="22" height="15" fill="none" stroke="#f4f7f8" stroke-width="2"/><path d="M2 6 L13 15 L24 6" fill="none" stroke="#f4f7f8" stroke-width="2"/></svg>
        www.TXShielded.com
      </p>
      <p class="link">
        <svg viewBox="0 0 26 26" aria-hidden="true"><g fill="none" stroke="#f4f7f8" stroke-width="1.6"><circle cx="13" cy="13" r="11"/><ellipse cx="13" cy="13" rx="5" ry="11"/><path d="M2 13 H24 M4 7 H22 M4 19 H22"/></g></svg>
        Rett@TXShielded.com
      </p>
    </div>
  </section>

  <section class="card card--front">
    <div class="crest-band"></div>
    <p class="site-top">TXShielded.com</p>
    <div class="emblem" role="img" aria-label="Scales of justice emblem in a glowing circle"></div>
    <p class="tagline">“Stand Firm With Your Counsel”</p>
    <h1 class="name">Everett Lansford</h1>
    <p class="title-strip">Attorney-at-Law</p>
    <div class="phones">
      <span class="toll">(844) TXShielded - Toll Free</span>
      <span>(844) 917-4403</span><span>(732) 604-1159</span>
      <span>(609) 481-7725</span><span>(908) 273-6641</span>
    </div>
    <div class="specialty-band"><p>“Aggressive Criminal Defense &amp; DUI Defense”</p></div>
  </section>

</body>
</html>
```